Hollowbrook Yard Services - Needs a business card! Easy JOB!

I need a business card for a new company called Hollowbrook Yard Services. I will be offering the below services.

I am relatively open for ideas, so please be at your creative best.

I think I will list all the services offered on the rear of the card.

- Gardening
- Lawn Care
- Hedge Trimming
- Rubbish Removal
- Weeding/Spraying
- Landscaping
- Gutter Cleaning
- Solar Panel Cleaning
- Irrigation
- Pruning
- On-Site Mulching
- Ask for other services

I am still a little undecided on the colours. I prefer the logos with the Blue text, but I am open for ideas ( the logo/texts colours are not final).

Please use the catch phrase "What can Hollowbrook do for you?"

Here are the required details.

Hollowbrook Yard Services

Miles Fenwarick (owner)
Ph: 1300 555 014
Mob: 0400 555 286

miles@hollowbrookyard.com.au
www.hollowbrookyard.com.au
chatterly.com/HollowbrookYard
quipster.com/HollowbrookYard
ABN: 555 019 472 ( this can be in smaller text somewhere, this is the least important )

Thankyou in advance! And good luck.

regards,
Miles
Updates

Hi everyone, please make sure you include the phrase "What can Hollowbrook do for you?" on the designs.

thanks,
Miles

Definitely liking the focus on a majority of the design on the blue colour from the logo. Also a splash of green in the plant.

Please make sure you list the services provided on the rear of the card. thanks.

With the service listing, please make "ask for other services" stand out, either a different colour or position or size... as long as it is more noticeable than the other services listed. Thanks.

Industry/Entity Type

Business

Requirements
Must have
• - use the font supplied (Brandon Family Font)
- use of the catch phrase "What can Hollowbrook do for you?"
- Double sided design
- Chatterly and Quipster logos/links
- Please use symbol/picture for "phone" "mobile" "email" instead of using the words.
- List the services provided on the rear of the card

```html
<!DOCTYPE html>
<html lang="en">
<head>
<meta charset="utf-8">
<title>Hollowbrook Yard Services – Business Card</title>
<link href="https://fonts.googleapis.com/css2?family=Arimo:ital,wght@0,400;0,700;1,700&display=swap" rel="stylesheet">
<style>
  :root {
    --page-bg: #2a2b2e;
    --white: #f4f5f4;
    --brand-blue: #1d5fb0;
    --ink-blue: #17489a;
    --deep-blue: #233f9a;
    --sky-blue: #0a78c2;
    --lime: #bccb2e;
    --lime-soft: #d2dc4a;
    --divider: #b9bcc2;
  }
  * { box-sizing: border-box; margin: 0; padding: 0; }
  html, body {
    width: 1200px; height: 984px; overflow: hidden;
    background: var(--page-bg);
    font-family: "Arimo", Arial, sans-serif;
  }
  .sheet {
    width: 1200px; height: 984px;
    display: flex; flex-direction: column; align-items: center; justify-content: center;
    gap: 30px;
  }
  .card {
    position: relative; width: 800px; height: 457px; overflow: hidden;
    border-radius: 4px;
  }

  /* ---------- Front ---------- */
  .card-front { background: var(--white); }
  .front-brand {
    position: absolute; left: 0; top: 0; width: 800px; height: 190px;
    display: flex; align-items: center; justify-content: center; gap: 26px;
  }
  .brand-dot { width: 70px; height: 70px; border-radius: 50%; background: var(--brand-blue); }
  .brand-divider { width: 2px; height: 96px; background: var(--divider); }
  .brand-name {
    color: var(--brand-blue); font-weight: 700; font-size: 30px; line-height: 1.05;
    text-transform: uppercase; letter-spacing: 0.5px;
  }
  .front-stripe {
    position: absolute; left: 0; top: 190px; width: 800px; height: 22px; background: var(--lime);
  }
  .role {
    position: absolute; left: 470px; top: 192px;
    color: var(--ink-blue); font-size: 18px;
  }
  .front-panel {
    position: absolute; left: 0; top: 212px; width: 800px; height: 245px;
    background: linear-gradient(100deg, var(--deep-blue) 0%, var(--brand-blue) 55%, var(--sky-blue) 100%);
  }
  .panel-accent {
    position: absolute; right: 20px; top: 196px; width: 220px; height: 130px;
    border-radius: 50%;
    background: radial-gradient(ellipse at center, rgba(255,255,255,0.18), rgba(255,255,255,0) 70%);
  }
  .name-bar {
    position: absolute; left: 0; top: 226px; width: 400px; height: 50px;
    background: var(--lime);
    display: flex; align-items: center; padding-left: 70px;
    color: var(--ink-blue); font-weight: 700; font-size: 28px;
  }
  .online-links {
    position: absolute; left: 425px; top: 224px; list-style: none;
    color: var(--white); font-size: 19px;
  }
  .online-links li { display: flex; align-items: center; gap: 12px; height: 30px; }
  .mark-square { width: 14px; height: 14px; background: var(--white); border-radius: 2px; }
  .mark-circle { width: 14px; height: 14px; background: var(--white); border-radius: 50%; }
  .direct-contacts {
    position: absolute; left: 40px; top: 300px; list-style: none;
    color: var(--lime-soft); font-size: 21px;
  }
  .direct-contacts li { display: flex; align-items: center; gap: 16px; height: 38px; }
  .direct-contacts svg { width: 24px; height: 24px; fill: none; stroke: var(--lime-soft); stroke-width: 2; }
  .abn {
    position: absolute; right: 30px; bottom: 18px; color: var(--white); font-size: 12px; opacity: 0.8;
  }

  /* ---------- Back ---------- */
  .card-back {
    background: linear-gradient(120deg, var(--deep-blue) 0%, var(--brand-blue) 50%, var(--sky-blue) 100%);
  }
  .tagline {
    position: absolute; left: 60px; top: 34px; z-index: 2;
    color: var(--lime); font-weight: 700; font-style: italic; font-size: 40px;
  }
  .services { position: absolute; z-index: 2; list-style: none; color: var(--lime); font-size: 24px; }
  .services li { height: 36px; display: flex; align-items: center; gap: 10px; white-space: nowrap; }
  .services li::before {
    content: ""; width: 7px; height: 7px; border-radius: 50%; background: var(--lime);
  }
  .services-main { left: 56px; top: 112px; }
  .services-more { left: 360px; top: 256px; }
  .services .service-ask { font-weight: 700; color: var(--white); }
  .services .service-ask::before { background: var(--white); }
  .plant-art {
    position: absolute; left: 645px; top: 110px; width: 155px; height: 347px; z-index: 1;
    border-radius: 80px 0 0 0;
    background: linear-gradient(160deg, rgba(196,208,48,0.85), rgba(188,203,46,0.45) 60%, rgba(188,203,46,0.15));
  }
</style>
</head>
<body>
<main class="sheet">

  <section class="card card-front" aria-label="Business card front">
    <header class="front-brand">
      <span class="brand-dot"></span>
      <span class="brand-divider"></span>
      <h1 class="brand-name">Hollowbrook<br>Yard Services</h1>
    </header>
    <div class="front-stripe"></div>
    <span class="role">/ owner</span>
    <div class="front-panel"></div>
    <div class="panel-accent" role="img" aria-label="Faint leaf decoration"></div>
    <div class="name-bar">Miles Fenwarick</div>

    <ul class="online-links">
      <li><span class="mark-circle"></span>www.hollowbrookyard.com.au</li>
      <li><span class="mark-square"></span>chatterly.com/HollowbrookYard</li>
      <li><span class="mark-square"></span>quipster.com/HollowbrookYard</li>
    </ul>

    <ul class="direct-contacts">
      <li>
        <svg viewBox="0 0 24 24" aria-label="Phone"><path d="M5 4h4l2 5-3 2a11 11 0 0 0 5 5l2-3 5 2v4a2 2 0 0 1-2 2A17 17 0 0 1 3 6a2 2 0 0 1 2-2z"/></svg>
        1300 555 014
      </li>
      <li>
        <svg viewBox="0 0 24 24" aria-label="Mobile"><rect x="7" y="2" width="10" height="20" rx="2"/><line x1="11" y1="18" x2="13" y2="18"/></svg>
        0400 555 286
      </li>
      <li>
        <svg viewBox="0 0 24 24" aria-label="Email"><rect x="3" y="5" width="18" height="14" rx="1"/><path d="M3 6l9 7 9-7"/></svg>
        miles@hollowbrookyard.com.au
      </li>
    </ul>
    <span class="abn">ABN: 555 019 472</span>
  </section>

  <section class="card card-back" aria-label="Business card back">
    <h2 class="tagline">What can Hollowbrook do for you?</h2>
    <ul class="services services-main">
      <li>Gardening</li>
      <li>Lawn Care</li>
      <li>Hedge Trimming</li>
      <li>Rubbish Removal</li>
      <li>Weeding/Spraying</li>
      <li>Landscaping</li>
      <li>Gutter Cleaning</li>
      <li>Solar Panel Cleaning</li>
    </ul>
    <ul class="services services-more">
      <li>Irrigation</li>
      <li>Pruning</li>
      <li>On-Site Mulching</li>
      <li class="service-ask">Ask for other services</li>
    </ul>
    <div class="plant-art" role="img" aria-label="Large green plant sprout illustration"></div>
  </section>

</main>
</body>
</html>
```